The Quillbrook Disinfecting Services

I need a logo that I will be able to send to printing company to make a magnet banner for my work vans. It should have my company name on it as well as website and phone number. Also a graphic of an electrostatic gun spraying schools. We provide electrostatic disinfecting for businesses so this would be perfect.
Thank you
Hvala

```html
<!DOCTYPE html>
<html lang="en">
<head>
<meta charset="utf-8">
<title>The Quillbrook Disinfecting Services – Van Magnet</title>
<link href="https://fonts.googleapis.com/css2?family=PT+Sans+Narrow:wght@700&family=Source+Sans+3:wght@700;800&display=swap" rel="stylesheet">
<style>
  :root {
    --navy: #2e3a63;
    --white: #ffffff;
    --grey: #666666;
    --ink: #121212;
    --page: #ffffff;
  }
  html, body {
    margin: 0;
    padding: 0;
    width: 1200px;
    height: 769px;
    overflow: hidden;
    background: var(--page);
  }
  .canvas {
    position: relative;
    width: 1200px;
    height: 769px;
  }
  .banner {
    position: absolute;
    left: 121px;
    top: 96px;
    width: 961px;
    height: 577px;
    background: var(--white);
    box-shadow: 0 0 30px rgba(0,0,0,0.12);
  }
  .banner__panel {
    position: absolute;
    left: 0;
    top: 0;
    width: 961px;
    height: 400px;
    background: var(--navy);
    border-radius: 0 0 20px 20px;
  }
  .headline {
    position: absolute;
    left: 38px;
    top: 66px;
    margin: 0;
    font-family: "Source Sans 3", "Myriad Pro", sans-serif;
    font-weight: 800;
    font-size: 84px;
    line-height: 79px;
    letter-spacing: -0.5px;
    color: var(--white);
  }
  .brand {
    position: absolute;
    left: 680px;
    top: 60px;
    width: 264px;
    text-align: right;
    color: var(--white);
    font-family: "PT Sans Narrow", sans-serif;
    font-weight: 700;
  }
  .brand__name {
    margin: 0;
    font-size: 50px;
    line-height: 54px;
  }
  .brand__tagline {
    margin: 56px 0 0;
    font-size: 17px;
    line-height: 20px;
  }
  .worker-art {
    position: absolute;
    left: 611px;
    top: 209px;
    width: 342px;
    height: 351px;
    border-radius: 12px;
    background: linear-gradient(160deg, #1e1e1e 0%, var(--ink) 70%, #2f8f45 100%);
  }
  .phone {
    position: absolute;
    left: 40px;
    top: 413px;
    margin: 0;
    font-family: "Source Sans 3", sans-serif;
    font-weight: 800;
    font-size: 92px;
    line-height: 100px;
    color: var(--grey);
    text-shadow: 3px 4px 0 var(--navy);
  }
  .website {
    position: absolute;
    left: 42px;
    top: 500px;
    margin: 0;
    font-family: "PT Sans Narrow", sans-serif;
    font-weight: 700;
    font-size: 42px;
    line-height: 50px;
    color: var(--navy);
  }
</style>
</head>
<body>
<div class="canvas">
  <div class="banner">
    <div class="banner__panel"></div>
    <h1 class="headline">We Provide<br>Electrostatic<br>Disinfecting<br>for Businesses</h1>
    <div class="brand">
      <p class="brand__name">The Quillbrook</p>
      <p class="brand__tagline">The Quillbrook Disinfecting Services</p>
    </div>
    <div class="worker-art" role="img" aria-label="Silhouette of a worker in a cap holding a green electrostatic disinfecting sprayer, standing over a dark oval shadow"></div>
    <p class="phone">408-555-0147</p>
    <p class="website">www.thequillbrookdc.com</p>
  </div>
</div>
</body>
</html>
```